Small consulting business needs a website designed to highlight value and four offerings

My company is a dynamic consulting firm with four Core Offerings: Learning & Evaluation, Program Management, Facilitation & Coaching; Implementation & Transformation. Our mission is to facilitate organizational change and transformation, and to make space for creativity, joy, belonging, and trust. If done successfully, we grow to better understand ourselves, each other, and the work we do together.

I'd like the website to give a feeling of confidence and clarity. I want the colors to match or compliment my logo. I want to have three tabs - Our Clients, Our Services, and Government.

See attached Word document for additional content. My current website is www.BrightHeronWorks.com.

Some websites I'm inspired by:
https://www.velmorgrove.com
https://www.tandemoakpartners.com
https://qzrb.org

Some websites of people/groups in my field that I find uninspiring:
http://dianacolfax.com
https://www.marbleway.org

Target Market(s)

State and local government agencies, health tech, and corporate HR departments

Industry/Entity Type

public health, aging, government, health tech

Coding

Coded - Design and coding required

Number of Pages Required

4 page

Font styles to use
Other font styles liked:
• Calibri and Merriweather

Colors
0054AA
0677BA
7BADD7
CADEEF
E8F1F8
00AB8E
00BBA5
67D7C9
C6EFE9
E9F9F6
FFC000
F8CF3A
FAE287
FDF2CF
FEFAEE
F0912C
F2A743
F7CA91
FBE8D2
FDF5EE

Requirements
Must have
• Attached logo and content, water colors few, and photos.
Nice to have
• Real pictures, which I can provide to the chosen designer
Should not have
• AI generated characters or cartoons.

```html
<!DOCTYPE html>
<html lang="en">
<head>
<meta charset="utf-8">
<title>Bright Heron Collaborative</title>
<link href="https://fonts.googleapis.com/css2?family=Merriweather:wght@300;400;700&family=Carlito:wght@400;700&display=swap" rel="stylesheet">
<style>
:root{
  --ink:#111111;
  --cream:#FFFBEF;
  --butter:#FDF2CF;
  --sun:#FAE287;
  --gold:#F8B92A;
  --gold-deep:#F0A21E;
  --sage:#7BA07A;
  --leaf:#A9D68E;
  --teal:#2F7A72;
  --line:#D9CFAF;
  --ghost:#E9DFC0;
  --dot:#FBE7A0;
}
*{margin:0;padding:0;box-sizing:border-box}
html,body{width:1200px;height:3771px;overflow:hidden}
body{
  position:relative;
  font-family:'Carlito',Calibri,sans-serif;
  color:var(--ink);
  background:
    radial-gradient(ellipse 700px 500px at 900px 1700px,rgba(250,226,135,.55),transparent 70%),
    radial-gradient(ellipse 800px 400px at 200px 1850px,rgba(250,226,135,.6),transparent 70%),
    radial-gradient(ellipse 900px 500px at 600px 200px,rgba(250,220,120,.75),transparent 70%),
    radial-gradient(ellipse 700px 400px at 300px 3550px,rgba(250,226,135,.55),transparent 70%),
    radial-gradient(ellipse 700px 400px at 950px 3600px,rgba(250,226,135,.5),transparent 70%),
    linear-gradient(180deg,#FCE9A6 0,#FEF4CF 700px,#FFFBEF 1100px,#FEF3CC 1500px,#FCE7A2 2000px,#FFFBEF 2120px,#FFFBEF 3250px,#FDEFC0 3771px);
}
.abs{position:absolute}
.serif{font-family:'Merriweather',Georgia,serif}
.dot{position:absolute;border-radius:50%;background:var(--dot);opacity:.85}

/* header */
.brand{left:137px;top:22px;display:flex;align-items:center;gap:8px}
.brand-mark{width:26px;height:26px;border-radius:50%;background:var(--gold)}
.brand-name{font-family:'Merriweather',Georgia,serif;font-size:16px;line-height:19px;color:#333}
.nav{left:390px;top:38px;display:flex;gap:40px;font-size:15px}
.nav span{white-space:nowrap}
.caret{display:inline-block;width:7px;height:7px;border-right:1.5px solid var(--ink);border-bottom:1.5px solid var(--ink);transform:rotate(45deg);margin-left:6px;position:relative;top:-3px}
.btn-projects{left:922px;top:20px;width:136px;height:47px;border:1.5px solid var(--gold);border-radius:24px;display:flex;align-items:center;justify-content:center;font-weight:700;font-size:14px;background:rgba(255,251,239,.4)}

/* hero */
.pill{left:475px;top:144px;width:250px;height:28px;border-radius:14px;background:rgba(250,214,110,.6);font-size:15px;display:flex;align-items:center;justify-content:center}
.hero-title{left:200px;top:186px;width:800px;text-align:center;font-family:'Merriweather',Georgia,serif;font-weight:300;font-size:43px;line-height:50px}
.service{position:absolute;width:260px}
.service h3{font-family:'Merriweather',Georgia,serif;font-weight:700;font-size:18px;margin-bottom:10px}
.service p{font-size:13px;line-height:20px}
.service.right{text-align:right}
.icon-ph{position:absolute;width:76px;height:76px;border-radius:50%}
.hero-art{left:498px;top:396px;width:205px;height:330px;border-radius:45% 45% 40% 40%;background:radial-gradient(ellipse at 50% 70%,#F8C23A,#F7D777 55%,#A7C98A 80%,rgba(167,201,138,0) 100%)}
.btn{position:absolute;height:42px;border-radius:21px;display:flex;align-items:center;justify-content:center;font-weight:700;font-size:13px}
.btn-green{left:446px;top:790px;width:149px;background:var(--leaf)}
.btn-gold{left:604px;top:790px;width:148px;background:var(--gold)}

/* story blocks */
.block-title{position:absolute;font-family:'Merriweather',Georgia,serif;font-weight:300;font-size:44px;line-height:52px}
.block-text{position:absolute;font-size:14px;line-height:20px}
.art{position:absolute;border-radius:50%}

/* rotating lists */
.section-title{position:absolute;left:0;width:1200px;text-align:center;font-family:'Merriweather',Georgia,serif;font-weight:300;font-size:44px;line-height:52px}
.roll{position:absolute;left:0;width:1200px;text-align:center;font-weight:700;font-size:37px;line-height:44px;text-transform:uppercase;white-space:nowrap}
.roll .ghost{color:transparent;-webkit-text-stroke:1.2px var(--ghost)}
.roll.faint{opacity:.55}
.tagline{position:absolute;left:0;width:1200px;text-align:center;font-family:'Merriweather',Georgia,serif;font-weight:300;font-size:58px;line-height:70px;color:var(--sage)}
.tagline .accent{color:var(--gold)}

/* footer */
.rule{position:absolute;left:140px;width:920px;height:1px;background:var(--line)}
.foot-col{position:absolute}
.foot-col h4{font-family:'Merriweather',Georgia,serif;font-weight:400;font-size:19px;margin-bottom:14px}
.foot-col li{list-style:none;font-size:13px;height:35px;display:flex;align-items:center;gap:12px}
.bullet{width:5px;height:5px;border-radius:50%;background:var(--gold)}
.soc{width:22px;height:22px;border-radius:50%;border:1px solid #999}
.soc.on{background:var(--gold);border-color:var(--gold)}
.foot-brand{left:880px;top:3610px;width:190px;text-align:center;font-family:'Merriweather',Georgia,serif;font-size:22px;line-height:32px;color:#333}
.copyright{left:0;top:3726px;width:1200px;text-align:center;font-size:13px}
</style>
</head>
<body>

<!-- decorative dots -->
<div class="dot" style="left:297px;top:187px;width:94px;height:94px"></div>
<div class="dot" style="left:840px;top:240px;width:90px;height:90px"></div>
<div class="dot" style="left:93px;top:967px;width:94px;height:94px"></div>
<div class="dot" style="left:831px;top:1262px;width:94px;height:94px"></div>
<div class="dot" style="left:88px;top:1603px;width:94px;height:94px"></div>
<div class="dot" style="left:733px;top:2064px;width:94px;height:94px"></div>
<div class="dot" style="left:338px;top:2664px;width:94px;height:94px"></div>
<div class="dot" style="left:93px;top:3199px;width:94px;height:94px"></div>

<!-- header -->
<header>
  <div class="abs brand"><span class="brand-mark"></span><span class="brand-name">Bright Heron<br>Collaborative</span></div>
  <nav class="abs nav"><span>Home</span><span>Our Services<i class="caret"></i></span><span>Our Clients</span><span>Government</span></nav>
  <div class="abs btn-projects">Our Projects</div>
</header>

<!-- hero -->
<section>
  <div class="abs pill">Here For You And Your Team.</div>
  <h1 class="abs hero-title">A Seat At The Table For Collaboration, Learning, And Meaningful Change.</h1>

  <div class="icon-ph" role="img" aria-label="Watercolor circles illustration for learning and evaluation" style="left:140px;top:385px;background:radial-gradient(circle,#E5B64A,#7FA98C 70%,rgba(127,169,140,0))"></div>
  <div class="service" style="left:140px;top:480px"><h3>Learning &amp; Evaluation</h3><p>Lorem Ipsum Dolor Sit Amet Consectetur.<br>Mauris Dictum Etiam Nec</p></div>

  <div class="icon-ph" role="img" aria-label="Watercolor wave illustration for facilitation and coaching" style="left:140px;top:587px;background:radial-gradient(circle,#F1C45A,#2F7A72 70%,rgba(47,122,114,0))"></div>
  <div class="service" style="left:140px;top:682px"><h3>Facilitation &amp; Coaching</h3><p>Lorem Ipsum Dolor Sit Amet Consectetur.<br>Mauris Dictum Etiam Nec</p></div>

  <div class="icon-ph" role="img" aria-label="Watercolor puzzle illustration for program management" style="left:984px;top:385px;background:radial-gradient(circle,#E8BD4D,#4E8B62 70%,rgba(78,139,98,0))"></div>
  <div class="service right" style="left:802px;top:480px"><h3>Program Management</h3><p>Lorem Ipsum Dolor Sit Amet Consectetur.<br>Mauris Dictum Etiam Nec</p></div>

  <div class="icon-ph" role="img" aria-label="Watercolor road at sunrise illustration for implementation" style="left:984px;top:587px;background:radial-gradient(circle,#F4C35A,#5F8F80 70%,rgba(95,143,128,0))"></div>
  <div class="service right" style="left:802px;top:682px"><h3>Implementation</h3><p>Lorem Ipsum Dolor Sit Amet Consectetur.<br>Mauris Dictum Etiam Nec</p></div>

  <div class="abs hero-art" role="img" aria-label="Large watercolor pineapple illustration"></div>

  <div class="btn btn-green">Our Services</div>
  <div class="btn btn-gold">Meet Our Clients</div>
</section>

<!-- mission / vision / value -->
<section>
  <h2 class="block-title" style="left:140px;top:996px">Our Mission</h2>
  <p class="block-text" style="left:143px;top:1068px;width:410px">Our mission is to facilitate organizational change and transformation, and to make space for creativity, joy, belonging, and trust. If done successfully, we grow to better understand ourselves, each other, and the work we do together.</p>
  <div class="art" role="img" aria-label="Watercolor illustration of a road leading to a sunrise framed by leaves" style="left:673px;top:970px;width:295px;height:250px;background:radial-gradient(ellipse,#E3A93C 0,#6FA99C 55%,rgba(111,169,156,0) 75%)"></div>

  <div class="art" role="img" aria-label="Watercolor illustration of overlapping circles" style="left:190px;top:1235px;width:275px;height:285px;background:radial-gradient(circle,#C9B85A 0,#4F8F86 50%,#E1C66E 65%,rgba(225,198,110,0) 75%)"></div>
  <h2 class="block-title" style="left:682px;top:1313px">Our Vision</h2>
  <p class="block-text" style="left:686px;top:1385px;width:350px">Our vision is to be part of a world where organizations and collaborators connect as human beings first. We envision a future where partners and colleagues strive for ongoing growth together.</p>

  <h2 class="block-title" style="left:133px;top:1630px">Our Value</h2>
  <p class="block-text" style="left:133px;top:1706px;width:430px;line-height:22.6px">We are the tranquility in chaos. The steady partner always at the table with you. We drive meaningful and measurable change, resulting in sustained progress towards key community outcomes and multi-sector initiatives. Our work produces values realignment, critical technical assistance, and develops strategic plans for innovative organizations ready to elevate their work.</p>
  <div class="art" role="img" aria-label="Watercolor burst illustration in green and orange" style="left:666px;top:1592px;width:330px;height:307px;background:radial-gradient(circle,rgba(255,251,239,0) 12%,#F2A743 30%,#2F7A5A 55%,rgba(47,122,90,0) 72%)"></div>
</section>

<!-- help -->
<section>
  <h2 class="section-title" style="top:2095px">We Help Your Team...</h2>
  <div class="roll faint" style="top:2178px"><span class="ghost">Turn bold visions into practical results.</span></div>
  <div class="roll" style="top:2234px"><span class="ghost">Empower teams to be better together.</span></div>
  <div class="roll" style="top:2289px">Transform conflict into opportunity.</div>
  <div class="roll" style="top:2345px"><span class="ghost">Strengthen community-led systems.</span></div>
  <div class="roll faint" style="top:2401px"><span class="ghost">Foster a sense of belonging...</span></div>
  <div class="tagline" style="top:2451px"><span class="accent">Find</span> Common Ground</div>
</section>

<!-- collaborate -->
<section>
  <div class="abs" role="img" aria-label="Small watercolor pineapple illustration" style="left:565px;top:2600px;width:58px;height:86px;border-radius:45%;background:radial-gradient(ellipse at 50% 65%,#F5C33F,#B5CF8E 75%,rgba(181,207,142,0))"></div>
  <h2 class="section-title" style="top:2701px">We Collaborate With</h2>
  <div class="roll faint" style="top:2791px"><span class="ghost">Large-scale companies</span></div>
  <div class="roll" style="top:2847px"><span class="ghost">National and local nonprofits</span></div>
  <div class="roll" style="top:2903px"><span class="ghost">State government agencies</span></div>
  <div class="roll" style="top:2958px">International partnerships &amp; organizations</div>
  <div class="roll" style="top:3014px"><span class="ghost">Foundations</span></div>
  <div class="roll" style="top:3069px"><span class="ghost">Tribal serving-organizations</span></div>
  <div class="roll faint" style="top:3121px"><span class="ghost">Startups in tech</span></div>
</section>

<!-- why -->
<section>
  <h2 class="block-title" style="left:140px;top:3237px">Why You Choose Us</h2>
  <p class="block-text" style="left:143px;top:3308px;width:900px;line-height:22px">Through our Core Offerings and guided by our founder’s traditional and nontraditional methods for engaging and steering a team, we create a sense of belonging, foster transparency, and help to build stronger relationships. Our approach helps to drive meaningful change so that organizations and initiatives can clear roadblocks and meet collective goals. Our team’s proven ability to transform conflict into opportunity will help to advance your organization and the communities you serve.</p>
</section>

<!-- footer -->
<footer>
  <div class="rule" style="top:3435px"></div>
  <div class="foot-col" style="left:143px;top:3488px"><h4>Quick Links</h4><ul>
    <li><i class="bullet"></i>Home</li><li><i class="bullet"></i>Our Services</li><li><i class="bullet"></i>Our Clients</li><li><i class="bullet"></i>Government</li></ul></div>
  <div class="foot-col" style="left:360px;top:3488px"><h4>Service Areas</h4><ul>
    <li><i class="bullet"></i>Learning &amp; Evaluation</li><li><i class="bullet"></i>Program Management</li><li><i class="bullet"></i>Facilitation &amp; Coaching</li><li><i class="bullet"></i>Implementation &amp; Transformation</li></ul></div>
  <div class="foot-col" style="left:672px;top:3488px"><h4>Social Media</h4><ul>
    <li><i class="soc on"></i>Friendsphere</li><li><i class="soc"></i>Viewcast</li><li><i class="soc"></i>Linkwork</li><li><i class="soc"></i>Snapgrid</li></ul></div>
  <div class="abs" style="left:945px;top:3490px;width:58px;height:58px;border-radius:50%;background:var(--gold)"></div>
  <div class="abs foot-brand">Bright Heron<br>Collaborative</div>
  <div class="rule" style="top:3697px"></div>
  <div class="abs copyright">Copyright © 2025 BrightHeron Inc. All Rights Reserved.</div>
</footer>

</body>
</html>
```